Norwegian psychologist service needs a fresh and exiting web site*

Norwegian psychologist service: working with therapy, personal development, mastery and personal growth. Focus: children and teenagers with special needs; family dynamics; group processes; individuals with a need for therapy and personal growth. (Our company name: Fjordlys og samhold (means Mastery and Growth).

We already have a logo for the company, which will be used (will be attached in the project).

The webside is to be structured in 4 pages with roll down curtain menus (the numbers are just for guiding the designer - the should not be added):

Page 1: Om Fjordlys og Samhold (about Mastery and Growth): this is where our business is is presented/described shortly: Lorem Ipsum dolor cit...

Page 2: Tjenester (Services): this is where our 5 service areas are presented:
2.1 Utredning (Investigation, diagnosing): Lorem Ipsum dolor cit...
2.2 Rådgivning (consulting): Lorem Ipsum dolor cit...

2.3 Kurs og work shops (courses and work shops): Lorem Ipsum dolor cit...
2.3a Fjordlys og samhold Tema 1 (T1)
2.3b Fjordlys og samhold Tema 2 (T2)
2.3c Fjordlys og samhold Tema 3 (T3)

2.4 Terapi og utvikling (Therapy and development)
2.4a Fjordlys og samhold for individer (FS1)
2.4b Fjordlys og samhold i familier (FS2)
2.4c Fjordlys og samhold i grupper (FS3)
2.4d Fjordlys og samhold i institusjoner (FS4)

Page 3: Aktuelt (Blog): this is our blog where we share knowledge and articles

Page 4: Kontakt (Contact): This is the contact form page. Contact form should constitute:
- Ditt navn (your name)
- E-post (your e-mail)
- Emne (subject)
- Melding (message/description)

Our project should also include suggestion for handheld units (iPhone, iPad).
Updates

We have both been traveling with work for a while, and then unfortunately both of us got sick on return, so we need a few more days to evaluate and choose design. Kind Regards Arvid & Margit

Target Market(s)

Focus on therapy, learning, mastery and growth for children and teenagers with special needs, within the family dynamics, or in a group setting.
OUR MARKETS:
Private market: individuals, families, groups and health industry institutions (with focus on learning, mastery, growth (as well as growing up) and psychiatry for children and teenagers with special difficulties and needs)
Public institutions: Government institutions, state institutions and municipality institutions (e.g. schools, municipality health service, hospitals) that serve the public (families with children and teenagers with special needs, and where learning, mastery, growth (as well as growing up) and potential psychiatry is an issue).

Number of Pages Required

4 page

Font styles to use
Sans Serif

Colors

Designer to choose colors to be used in the design.

Requirements
Must have
• The website must have 4 pages with roll down curtain menus (we have added a PDF with suggested structure, and headings, with sub menus - see attached PDF drawing.
• The web page must also use the added logo file - and make the web page work well with our logo.
• We would like the website to have a modern look and we would like the site to be associated with typical HIGH END TOP QUALITY private health institutions, but with a stronger focus on human beings (hands, faces etc), and not white coats and doctors. We are psychologists in the private market.
• For instance, if photos are being used - we tend to like "warm" almost art-like, "grainy" two-tone (e.g. sepia) photos to illustrate our focus. If designer can find such photos as part of design, it would be interesting to us. We would like a few photos like that integrated in the design.
• We also want a design suggestion for how the web page should look like and behave on handheld units (e.g. iPhone, iPad).
Nice to have
• If designer could find a number of suitable photos that matches the business idea and design requirements (see description above), that could follow website, that would be good.
• It could also be nice to have graphic symbols that denote the different pages/subpages (subjects)....
• HORSES: we sometimes use horses as a "tool" in therapy sessions. The horse is not necessarily used for riding, but for contact, communication and grooming. PHOTOS: we would like the designer to find an opportunity for using a photo reflecting this cooperation between therapist, child, teenager and horse. It is a bit up to the designer to find a way to do this... Since the horse is only a tool, among many other tools, it does not have to be much - but we want to try and see how it will work with a photo that also reflects this part of our business.

```html
<!DOCTYPE html>
<html lang="en">
<head>
<meta charset="utf-8">
<title>Fjordlys og samhold</title>
<link href="https://fonts.googleapis.com/css2?family=Poppins:wght@300;400;500;600;700&family=Dancing+Script:wght@700&display=swap" rel="stylesheet">
<style>
:root{
  --navy:#2d3992;
  --navy-dark:#232d7a;
  --green:#0c6a36;
  --green-dark:#08552a;
  --ink:#2b2b33;
  --text:#4a4a52;
  --muted:#8a8a92;
  --topbar:#f4f4f4;
  --line:#e5e5e8;
  --footer:#1f2024;
  --footer-bottom:#17181b;
  --white:#ffffff;
}
*{margin:0;padding:0;box-sizing:border-box}
html,body{width:1200px;height:2844px;overflow:hidden}
body{position:relative;font-family:'Poppins',sans-serif;color:var(--text);background:var(--white)}
.abs{position:absolute}
.script{font-family:'Dancing Script',cursive;font-weight:700;color:var(--green)}
.btn{position:absolute;display:flex;align-items:center;justify-content:center;color:var(--white);font-size:9.5px;font-weight:700;text-transform:uppercase;letter-spacing:.2px;border-radius:2px}
.btn-green{background:var(--green);box-shadow:0 3px 0 var(--green-dark)}
.btn-navy{background:var(--navy);box-shadow:0 3px 0 var(--navy-dark)}

/* top bar */
.topbar{top:0;left:0;width:1200px;height:29px;background:var(--topbar);font-size:9.5px;color:#444}
.topbar span{position:absolute;top:9px;display:flex;align-items:center;gap:5px}
.header{top:29px;left:0;width:1200px;height:63px;background:var(--white)}
.brand{position:absolute;left:234px;top:13px;display:flex;align-items:center;gap:8px}
.brand-mark{width:34px;height:34px;border-radius:50%;background:var(--navy)}
.brand-name{font-size:19px;font-weight:500;color:var(--navy);letter-spacing:.2px}
.header-call{position:absolute;left:620px;top:19px;font-size:19px;color:var(--navy)}
.header-call b{font-weight:600}
.nav{top:92px;left:0;width:1200px;height:29px;background:var(--navy)}
.nav ul{list-style:none;position:absolute;left:234px;top:0;display:flex;height:29px;border-left:1px solid rgba(255,255,255,.2)}
.nav li{color:var(--white);font-size:9px;font-weight:600;text-transform:uppercase;padding:0 18px;line-height:29px;border-right:1px solid rgba(255,255,255,.2)}

/* hero */
.hero{top:121px;left:0;width:1200px;height:370px;background:linear-gradient(90deg,#5d6163 0%,#9a9ea0 35%,#c9c7c2 60%,#b8aea3 80%,#8d8279 100%)}
.hero-shade{top:491px;left:0;width:1200px;height:6px;background:#d9d9db}
.hero-tag{left:235px;top:214px;font-size:23px;color:var(--white)}
.hero-title{left:234px;top:250px;font-size:38px;line-height:45px;color:var(--white);font-weight:400;letter-spacing:.3px}
.slider-arrow{position:absolute;width:44px;height:44px;background:rgba(255,255,255,.85);color:#888;font-size:12px;display:flex;align-items:center;justify-content:center}
.hero-down{left:586px;top:484px;width:28px;height:28px;border-radius:50%;background:var(--white)}

/* about */
.about-photo-main{left:285px;top:543px;width:271px;height:375px;background:linear-gradient(160deg,#e8e6e2,#d8c6b6 50%,#b9b0a8)}
.about-photo-small{left:234px;top:779px;width:255px;height:188px;background:linear-gradient(120deg,#d7d4d0,#b5aba3 50%,#e6e4e2);outline:6px solid var(--white)}
.know-more{left:223px;top:649px;width:104px;height:104px;border-radius:50% 50% 0 50%;background:var(--navy);color:var(--white);text-align:center;padding-top:35px}
.know-more b{display:block;font-size:12.5px;font-weight:600}
.know-more i{display:block;font-family:'Dancing Script',cursive;font-size:20px;font-style:normal;margin-top:-2px}
.eyebrow{font-size:22px}
.h2{font-size:21px;font-weight:500;color:var(--ink)}
.lead{font-size:13.5px;font-weight:500;color:var(--ink);line-height:18.5px}
.body-copy{font-size:10.5px;line-height:18.8px;color:var(--text)}

/* services */
.services{top:1032px;left:0;width:1200px;height:655px;background:linear-gradient(90deg,#d9dbdd 0%,#e4e4e4 40%,#ececed 60%,#efefef 100%)}
.services-photo{top:1032px;left:0;width:620px;height:655px;background:linear-gradient(100deg,#c9ced3 0%,#d8c3a6 40%,#a9b8d1 70%,rgba(236,236,237,0) 100%)}
.svc-card{position:absolute;width:178px;height:178px;background:var(--white);text-align:center}
.svc-icon{width:50px;height:50px;border-radius:50%;background:var(--navy);margin:18px auto 12px;display:flex;align-items:center;justify-content:center}
.svc-card h3{font-size:13px;font-weight:500;color:var(--ink);line-height:19px}
.svc-card p{font-size:8.5px;line-height:15px;color:var(--text);padding:6px 12px 0}

/* blog */
.section-title{width:1200px;left:0;text-align:center}
.feature-post{left:234px;top:1814px;width:357px;height:263px;background:linear-gradient(135deg,#eceae8 0%,#d7d0c8 45%,#7c8cae 75%,#3a4796 100%)}
.feature-post-overlay{left:234px;top:1950px;width:357px;height:127px;background:linear-gradient(180deg,rgba(45,57,146,0),rgba(45,57,146,.92))}
.meta{display:flex;gap:14px;font-size:9px;font-weight:500;color:var(--ink);align-items:center}
.meta span{display:flex;align-items:center;gap:4px}
.post-thumb{position:absolute;left:609px;width:125px;height:78px}
.post-item{position:absolute;left:750px;width:216px}
.post-item h4{font-size:13px;font-weight:500;color:var(--ink);margin:5px 0 4px}
.post-item p{font-size:8.8px;line-height:15px;color:var(--text)}

/* testimonials */
.testimonials{top:2134px;left:0;width:1200px;height:445px;background:#eef2f3}
.testimonials-photo{top:2134px;left:760px;width:440px;height:445px;background:linear-gradient(90deg,rgba(238,242,243,0) 0%,#ddd6d0 50%,#cfc7c0 100%)}
.quote-card{position:absolute;top:2274px;width:357px;height:138px;background:var(--white)}
.quote-card .mark{position:absolute;left:19px;top:20px;font-size:30px;color:var(--green);font-family:Georgia,serif;line-height:1}
.quote-card p{position:absolute;left:48px;top:33px;width:290px;font-size:13.5px;line-height:19px;color:var(--text)}
.quote-card::after{content:"";position:absolute;left:34px;bottom:-10px;border-left:10px solid transparent;border-right:10px solid transparent;border-top:10px solid var(--white)}
.client-name{position:absolute;top:2436px;font-size:10px;font-weight:600;color:var(--navy)}
.client-age{position:absolute;top:2452px;font-size:10px;color:var(--muted)}
.dots{left:567px;top:2521px;display:flex;gap:7px}
.dots i{width:5px;height:5px;border-radius:50%;background:#b9c0e0}
.dots i:first-child{background:var(--navy)}

/* footer */
.footer{top:2579px;left:0;width:1200px;height:222px;background:var(--footer);color:#d8d8da}
.footer-bottom{top:2801px;left:0;width:1200px;height:43px;background:var(--footer-bottom);color:#e6e6e6;font-size:9.5px;text-align:center;line-height:43px}
.footer-bottom em{font-style:normal;color:var(--green)}
.f-head{position:absolute;top:2620px;font-size:11px;font-weight:600;color:var(--white);text-transform:uppercase}
.f-text{font-size:9px;line-height:16px;color:#d8d8da}
.social{position:absolute;top:2741px;width:24px;height:24px;border-radius:50%;border:1px solid #cfcfd2}
.quick-links{position:absolute;left:478px;top:2651px;list-style:none;font-size:9px;color:#d8d8da}
.quick-links li{height:22.5px}
.quick-links li::before{content:"›";display:inline-block;width:12px;color:#aaa}
.contact-row{position:absolute;left:594px;display:flex;gap:10px;font-size:9px;line-height:16px;color:#e2e2e4}
.contact-row .ic{width:20px;height:20px;border-radius:50%;background:var(--green);flex:none;display:flex;align-items:center;justify-content:center}
.newsletter{left:797px;top:2652px;width:168px;height:97px;background:#27282d;padding:13px 12px}
.newsletter p{font-size:9px;line-height:15px;color:#e6e6e6}
.email-field{position:absolute;left:11px;top:55px;width:106px;height:23px;background:var(--white);border-radius:12px 0 0 12px;font-size:8.5px;color:#999;display:flex;align-items:center;gap:5px;padding-left:10px}
.email-send{position:absolute;left:117px;top:53px;width:36px;height:27px;border-radius:14px;background:var(--green);display:flex;align-items:center;justify-content:center}
</style>
</head>
<body>

<!-- top bar -->
<div class="abs topbar">
  <span style="left:234px"><svg width="9" height="9" viewBox="0 0 10 10"><circle cx="5" cy="5" r="4" fill="none" stroke="#0c6a36" stroke-width="1.3"/><path d="M5 2.5V5h2" stroke="#0c6a36" stroke-width="1.1" fill="none"/></svg>Visit Us Daily from 9:00am to 7:00pm</span>
  <span style="left:628px"><svg width="8" height="10" viewBox="0 0 8 10"><path d="M4 0a3.5 3.5 0 0 0-3.5 3.5C.5 6 4 10 4 10s3.5-4 3.5-6.5A3.5 3.5 0 0 0 4 0z" fill="#0c6a36"/><circle cx="4" cy="3.5" r="1.2" fill="#fff"/></svg>48 Fjordveien, Bergen, Norway, 5003</span>
  <span style="left:832px"><svg width="10" height="8" viewBox="0 0 10 8"><rect x=".5" y=".5" width="9" height="7" fill="#0c6a36"/><path d="M.5 .8 5 4.5 9.5.8" stroke="#fff" fill="none"/></svg>kontakt@fjordlysogsamhold.no</span>
</div>

<!-- header -->
<header class="abs header">
  <div class="brand"><div class="brand-mark"></div><div class="brand-name">Fjordlys og samhold</div></div>
  <div class="header-call">Call: <b>555 214 7830</b></div>
  <div class="btn btn-green" style="left:812px;top:13px;width:154px;height:32px">Make an appointment</div>
</header>

<nav class="abs nav">
  <ul>
    <li>Home</li><li>About Fjordlys og Samhold</li><li>Services</li><li>Blog</li><li>Contact</li>
  </ul>
  <svg class="abs" style="left:951px;top:8px" width="13" height="13" viewBox="0 0 13 13"><circle cx="5.5" cy="5.5" r="4.3" fill="none" stroke="#fff" stroke-width="1.4"/><path d="M8.7 8.7 12 12" stroke="#fff" stroke-width="1.5"/></svg>
</nav>

<!-- hero -->
<div class="abs hero" role="img" aria-label="Smiling couple embracing in a bright counselling room, seen over the shoulder of a therapist"></div>
<div class="abs hero-shade"></div>
<div class="slider-arrow" style="left:0;top:287px">‹</div>
<div class="slider-arrow" style="left:1156px;top:287px">›</div>
<div class="abs script hero-tag">I could help you to</div>
<h1 class="abs hero-title">PSYCHOLOGICAL CARE<br>AT THE HIGHEST LEVEL</h1>
<div class="btn btn-green" style="left:234px;top:360px;width:153px;height:34px">Make an appointment</div>
<div class="btn btn-navy" style="left:397px;top:360px;width:76px;height:34px">About us</div>
<div class="abs hero-down"><svg width="28" height="28" viewBox="0 0 28 28"><path d="M11 13l3 3 3-3" stroke="#aaa" fill="none"/></svg></div>

<!-- about -->
<div class="abs about-photo-main" role="img" aria-label="Portrait of a smiling woman resting her chin on her hand"></div>
<div class="abs about-photo-small" role="img" aria-label="Couple shaking hands with a counsellor during a session"></div>
<div class="abs know-more"><b>Know More</b><i>about us</i></div>

<div class="abs script eyebrow" style="left:591px;top:544px">about us</div>
<h2 class="abs h2" style="left:591px;top:572px">We Are The Best Support for You</h2>
<p class="abs lead" style="left:591px;top:613px;width:380px">Lorem ipsum dolor sit amet, consectetur adipiscing elit. Aenean sit amet pretium nisi. Aenean turpis neque, volutpat at felis eu, iaculis imperdiet neque.</p>
<p class="abs body-copy" style="left:591px;top:680px;width:376px">Ut accumsan felis purus. Donec consequat condimentum bibendum. Phasellus ultricies molestie eros id volutpat. Nullam a lacinia nisl. Aliquam vestibulum massa ut dolor tincidunt, ac vulputate magna dignissim. Integer nec leo nec sem luctus rhoncus. Phasellus blandit iaculis enim, sit amet bibendum odio semper vitae.</p>
<p class="abs body-copy" style="left:591px;top:793px;width:376px">In quis nunc odio. Praesent sit amet velit velit. Morbi ornare risus quis magna pharetra, vel pulvinar risus rhoncus. Pellentesque diam metus, tincidunt sed tincidunt at, interdum eget quam. Aliquam ornare varius quam sit amet luctus. Vivamus facilisis vehicula sapien quis ultricies.</p>
<div class="abs" style="left:591px;top:885px;width:375px;height:1px;background:var(--line)"></div>
<div class="abs" style="left:591px;top:911px;font-size:10.5px;color:var(--navy)">Call for book an appointment</div>
<div class="abs" style="left:591px;top:926px;font-size:20px;font-weight:600;color:var(--navy)">555 214 7830</div>
<div class="btn btn-green" style="left:763px;top:910px;width:152px;height:34px">Make an appointment</div>

<!-- services -->
<div class="abs services"></div>
<div class="abs services-photo" role="img" aria-label="Smiling blonde therapist in a light blue blouse taking notes"></div>
<div class="abs script eyebrow" style="left:591px;top:1096px">my services</div>
<h2 class="abs h2" style="left:591px;top:1125px">What Service Provide</h2>
<p class="abs lead" style="left:591px;top:1166px;width:380px">Lorem ipsum dolor sit amet, consectetur adipiscing elit. Aenean sit amet pretium nisi.</p>

<div class="svc-card" style="left:591px;top:1236px">
  <div class="svc-icon"><svg width="22" height="24" viewBox="0 0 22 24"><rect x="3" y="3" width="16" height="19" rx="1.5" fill="none" stroke="#fff" stroke-width="1.4"/><rect x="7.5" y="1" width="7" height="4" rx="1" fill="#2d3992" stroke="#fff" stroke-width="1.2"/><path d="M7 10h8M7 14h8M7 18h5" stroke="#fff" stroke-width="1.2"/></svg></div>
  <h3>Investigation,<br>Diagnosing</h3>
  <p>Lorem ipsum dolor sit amet, consectetur adipiscing elit. Aenean sit amet pretium nisi.</p>
</div>
<div class="svc-card" style="left:786px;top:1236px">
  <div class="svc-icon"><svg width="24" height="24" viewBox="0 0 24 24"><circle cx="9" cy="9" r="4" fill="none" stroke="#fff" stroke-width="1.4"/><path d="M2 21c1-4 4-6 7-6s6 2 7 6" fill="none" stroke="#fff" stroke-width="1.4"/><rect x="14" y="2" width="8" height="6" rx="1.5" fill="none" stroke="#fff" stroke-width="1.2"/></svg></div>
  <h3>Consulting</h3>
  <p>Lorem ipsum dolor sit amet, consectetur adipiscing elit. Aenean sit amet pretium nisi.</p>
</div>
<div class="svc-card" style="left:591px;top:1433px">
  <div class="svc-icon"><svg width="24" height="24" viewBox="0 0 24 24"><rect x="7" y="3" width="15" height="11" fill="none" stroke="#fff" stroke-width="1.3"/><path d="M10 10l3-3 2 2 4-4" fill="none" stroke="#fff" stroke-width="1.2"/><circle cx="5" cy="11" r="2.3" fill="none" stroke="#fff" stroke-width="1.3"/><path d="M1 22v-5c0-2 2-3 4-3s4 1 4 3v5" fill="none" stroke="#fff" stroke-width="1.3"/></svg></div>
  <h3>Courses and<br>Work Shops</h3>
  <p>Lorem ipsum dolor sit amet, consectetur adipiscing elit. Aenean sit amet pretium nisi.</p>
</div>
<div class="svc-card" style="left:786px;top:1433px">
  <div class="svc-icon"><svg width="24" height="24" viewBox="0 0 24 24"><circle cx="12" cy="5" r="3" fill="none" stroke="#fff" stroke-width="1.3"/><path d="M6 14c1-3 3-5 6-5s5 2 6 5" fill="none" stroke="#fff" stroke-width="1.3"/><rect x="3" y="15" width="18" height="4" rx="1" fill="none" stroke="#fff" stroke-width="1.3"/><path d="M5 19v3M19 19v3" stroke="#fff" stroke-width="1.3"/></svg></div>
  <h3>Therapy and<br>Development</h3>
  <p>Lorem ipsum dolor sit amet, consectetur adipiscing elit. Aenean sit amet pretium nisi.</p>
</div>

<!-- blog -->
<div class="abs section-title script eyebrow" style="top:1731px">our blog</div>
<h2 class="abs section-title" style="top:1759px;font-size:20px;font-weight:600;color:var(--ink)">LATEST NEWS</h2>

<div class="abs feature-post" role="img" aria-label="Woman lying on a sofa talking with a therapist holding a notepad"></div>
<div class="abs feature-post-overlay"></div>
<div class="abs meta" style="left:257px;top:2000px;color:#fff">
  <span><svg width="9" height="9" viewBox="0 0 10 10"><circle cx="5" cy="5" r="4" fill="none" stroke="#fff" stroke-width="1.3"/><path d="M5 2.5V5h2" stroke="#fff" fill="none"/></svg>08 Feb, 2020</span>
  <span><svg width="11" height="9" viewBox="0 0 11 9"><ellipse cx="5.5" cy="4" rx="5" ry="3.5" fill="none" stroke="#fff" stroke-width="1.2"/></svg>23 Comments</span>
</div>
<div class="abs" style="left:257px;top:2019px;width:320px;font-size:13px;line-height:18px;font-weight:500;color:#fff">Lorem ipsum dolor sit amet, consectetur adipiscing elit.</div>

<div class="post-thumb" style="top:1814px;background:linear-gradient(135deg,#dfe4ea,#b79d86 50%,#7d94bd)" role="img" aria-label="Happy couple sitting close together on a sofa"></div>
<div class="post-item" style="top:1816px">
  <div class="meta"><span><svg width="9" height="9" viewBox="0 0 10 10"><circle cx="5" cy="5" r="4" fill="none" stroke="#0c6a36" stroke-width="1.3"/><path d="M5 2.5V5h2" stroke="#0c6a36" fill="none"/></svg>08 Feb, 2020</span><span><svg width="11" height="9" viewBox="0 0 11 9"><ellipse cx="5.5" cy="4" rx="5" ry="3.5" fill="none" stroke="#2d3992" stroke-width="1.2"/></svg>23 Comments</span></div>
  <h4>Ut accumsan felis purus</h4>
  <p>Lorem ipsum dolor sit amet, consectetur adipiscing elit. Aenean sit amet pretium nisi.</p>
</div>

<div class="post-thumb" style="top:1906px;background:linear-gradient(135deg,#d6d8da,#8e877f 50%,#c8c6c2)" role="img" aria-label="Therapist listening to a client seated on a grey couch"></div>
<div class="post-item" style="top:1908px">
  <div class="meta"><span><svg width="9" height="9" viewBox="0 0 10 10"><circle cx="5" cy="5" r="4" fill="none" stroke="#0c6a36" stroke-width="1.3"/><path d="M5 2.5V5h2" stroke="#0c6a36" fill="none"/></svg>08 Feb, 2020</span><span><svg width="11" height="9" viewBox="0 0 11 9"><ellipse cx="5.5" cy="4" rx="5" ry="3.5" fill="none" stroke="#2d3992" stroke-width="1.2"/></svg>23 Comments</span></div>
  <h4>Nulla porttitor quam in justo</h4>
  <p>Lorem ipsum dolor sit amet, consectetur adipiscing elit. Aenean sit amet pretium nisi.</p>
</div>

<div class="post-thumb" style="top:1997px;background:linear-gradient(135deg,#cfc9c2,#8f7c6c 50%,#b8c2d3)" role="img" aria-label="Counsellor comforting an older man during a session"></div>
<div class="post-item" style="top:1999px">
  <div class="meta"><span><svg width="9" height="9" viewBox="0 0 10 10"><circle cx="5" cy="5" r="4" fill="none" stroke="#0c6a36" stroke-width="1.3"/><path d="M5 2.5V5h2" stroke="#0c6a36" fill="none"/></svg>08 Feb, 2020</span><span><svg width="11" height="9" viewBox="0 0 11 9"><ellipse cx="5.5" cy="4" rx="5" ry="3.5" fill="none" stroke="#2d3992" stroke-width="1.2"/></svg>23 Comments</span></div>
  <h4>Duis nec mollis tortor</h4>
  <p>Lorem ipsum dolor sit amet, consectetur adipiscing elit. Aenean sit amet pretium nisi.</p>
</div>

<!-- testimonials -->
<div class="abs testimonials"></div>
<div class="abs testimonials-photo" role="img" aria-label="Faded portrait of a smiling woman"></div>
<div class="abs section-title script eyebrow" style="top:2177px">testimonials</div>
<h2 class="abs section-title h2" style="top:2205px">Happy Clients About Me</h2>

<div class="quote-card" style="left:234px"><span class="mark">“</span><p>Lorem ipsum dolor sit amet, consectetur adipiscing elit. Aenean sit amet pretium nisi. Aenean turpis neque, volutpat at felis eu, iaculis imperdiet neque.</p></div>
<div class="quote-card" style="left:609px"><span class="mark">“</span><p>Lorem ipsum dolor sit amet, consectetur adipiscing elit. Aenean sit amet pretium nisi. Aenean turpis neque, volutpat at felis eu, iaculis imperdiet neque.</p></div>
<div class="client-name" style="left:264px">EIRIK DAHL</div>
<div class="client-age" style="left:264px">25 years</div>
<div class="client-name" style="left:639px">EIRIK DAHL</div>
<div class="client-age" style="left:639px">25 years</div>
<div class="abs dots"><i></i><i></i><i></i><i></i><i></i><i></i></div>

<!-- footer -->
<footer class="abs footer"></footer>
<div class="abs" style="left:234px;top:2622px;display:flex;align-items:center;gap:7px">
  <div style="width:26px;height:26px;border-radius:50%;background:var(--navy)"></div>
  <div style="font-size:15px;font-weight:500;color:var(--navy)">Fjordlys og samhold</div>
</div>
<p class="abs f-text" style="left:234px;top:2682px;width:200px">Lorem ipsum dolor sit amet, consectetur adipiscing elit. Etiam efficitur dolor massa, ac molestie sem lacinia vel.</p>
<div class="social" style="left:235px"></div>
<div class="social" style="left:267px"></div>
<div class="social" style="left:299px"></div>

<div class="f-head" style="left:471px">Quick Links</div>
<ul class="quick-links"><li>Home</li><li>About Us</li><li>Services</li><li>Blog</li><li>Contact Us</li></ul>

<div class="f-head" style="left:595px">Get in Touch</div>
<div class="contact-row" style="top:2650px"><span class="ic"><svg width="10" height="10" viewBox="0 0 10 10"><path d="M2 1l2 2-1 1.3c.6 1.2 1.5 2.1 2.7 2.7L7 6l2 2-1.3 1.3C4.5 9 1 5.5.7 2.3z" fill="#fff"/></svg></span><span style="padding-top:2px">+ 47 800 21 400</span></div>
<div class="contact-row" style="top:2683px"><span class="ic"><svg width="10" height="8" viewBox="0 0 10 8"><rect x=".5" y=".5" width="9" height="7" fill="#fff"/><path d="M.5.8 5 4.5 9.5.8" stroke="#0c6a36" fill="none"/></svg></span><span style="padding-top:2px">post@fjordlys.no</span></div>
<div class="contact-row" style="top:2717px"><span class="ic"><svg width="8" height="10" viewBox="0 0 8 10"><path d="M4 0a3.5 3.5 0 0 0-3.5 3.5C.5 6 4 10 4 10s3.5-4 3.5-6.5A3.5 3.5 0 0 0 4 0z" fill="#fff"/><circle cx="4" cy="3.5" r="1.2" fill="#0c6a36"/></svg></span><span style="padding-top:2px">48 Fjordveien, Sentrum,<br>Bergen, 5003</span></div>

<div class="f-head" style="left:797px">Newsletter</div>
<div class="abs newsletter">
  <p>Enter your email to receive updates and specials</p>
  <div class="email-field"><svg width="10" height="8" viewBox="0 0 10 8"><rect x=".5" y=".5" width="9" height="7" fill="none" stroke="#999"/><path d="M.5.8 5 4.5 9.5.8" stroke="#999" fill="none"/></svg>Email Address</div>
  <div class="email-send"><svg width="13" height="13" viewBox="0 0 13 13"><path d="M1 6l11-5-4 11-2-4z" fill="#fff"/></svg></div>
</div>

<div class="abs footer-bottom">Copyright © 2020 <em>Fjordlys og samhold</em>. All Rights Reserved</div>

</body>
</html>
```